Brindle Offers is an online marketing platform.

A daily deals site for consumers a way to bring in new clients for clients and this is who the business cards are for. Industries - Food and Drink, Things To Do, Beauty and Spas, Staycations and Services.
Logo on one side.
Name - Owen Radley
Job Title - Sales Director
Phone Number - 07912358046
Email - owen@brindleoffers.co.uk
need same for second person
Name - Fiona Bracken
Job Title - Operations Director
Phone Number - 01632840275
Email - fiona@brindleoffers.co.uk
Bottom Right - Chatterbook Icon, Snapa Icon, Pipline Icon
Target Market(s)
Business owners of the above industries
Contact Information for Business Card
Name - Owen Radley
Name - Fiona Bracken
Look and feel

```html
<!DOCTYPE html>
<html lang="en">
<head>
<meta charset="utf-8">
<title>Brindle Offers – Business Card</title>
<link rel="stylesheet" href="https://fonts.googleapis.com/css2?family=Josefin+Sans:wght@400;600;700&display=swap">
<style>
  :root {
    --backdrop: #2a2a2a;
    --card-light: #ffffff;
    --card-dark: #1c1c1c;
    --brand-blue: #0f57a6;
    --ink-grey: #4a4a4a;
    --ring-grey: #5c5c5c;
    --social-1: #3b5998;
    --social-2: #55acee;
    --social-3: #5b3f3a;
    --white: #ffffff;
  }
  * { box-sizing: border-box; margin: 0; padding: 0; }
  html, body {
    width: 1200px; height: 977px; overflow: hidden;
    background: var(--backdrop);
    font-family: "Josefin Sans", sans-serif;
  }
  .canvas { position: relative; width: 1200px; height: 977px; }

  .card {
    position: absolute; width: 700px; height: 400px;
    box-shadow: 4px 6px 10px rgba(0,0,0,0.55);
  }
  .card--front { left: 154px; top: 64px; background: var(--card-light); }
  .card--back { left: 290px; top: 512px; background: var(--card-dark); }

  /* Front */
  .brand-lockup {
    position: absolute; left: 88px; top: 160px;
    display: flex; align-items: center; gap: 12px;
  }
  .brand-mark {
    width: 56px; height: 56px; border-radius: 50%;
    border: 6px solid var(--brand-blue);
  }
  .brand-name {
    font-weight: 700; font-size: 32px; color: var(--brand-blue);
    line-height: 1; padding-top: 6px; white-space: nowrap;
  }
  .divider {
    position: absolute; left: 400px; top: 139px;
    width: 2px; height: 124px; background: var(--ink-grey);
  }
  .contact { position: absolute; left: 428px; top: 143px; color: var(--ink-grey); }
  .contact__name {
    font-weight: 700; font-size: 26px; color: var(--brand-blue);
    letter-spacing: 0.5px; line-height: 1;
  }
  .contact__role { font-size: 19px; margin-top: 6px; line-height: 1; }
  .contact__list { list-style: none; margin-top: 22px; }
  .contact__item {
    display: flex; align-items: center; gap: 14px;
    font-size: 19px; line-height: 1; margin-bottom: 11px;
  }
  .contact__icon { width: 14px; height: 14px; fill: var(--brand-blue); flex: none; }

  .socials {
    position: absolute; right: 48px; top: 334px;
    display: flex; gap: 12px; list-style: none;
    font-size: 10px; color: var(--ink-grey);
  }
  .socials__item { display: flex; align-items: center; gap: 4px; }
  .socials__dot { width: 16px; height: 16px; border-radius: 50%; }
  .socials__dot--chatter { background: var(--social-1); }
  .socials__dot--pipline { background: var(--social-2); }
  .socials__dot--snapa { background: var(--social-3); }

  /* Back */
  .back-art { position: absolute; inset: 0; }
  .back-url {
    font-family: "Josefin Sans", sans-serif; font-weight: 600;
    font-size: 22px; fill: var(--white); letter-spacing: 2px;
  }
  .back-name {
    font-family: "Josefin Sans", sans-serif; font-weight: 700;
    font-size: 30px; fill: var(--brand-blue);
  }
</style>
</head>
<body>
<main class="canvas">
  <section class="card card--front" aria-label="Business card front">
    <div class="brand-lockup">
      <span class="brand-mark" aria-hidden="true"></span>
      <span class="brand-name">Brindle Offers</span>
    </div>
    <div class="divider"></div>
    <div class="contact">
      <h1 class="contact__name">OWEN RADLEY</h1>
      <p class="contact__role">Sales Director</p>
      <ul class="contact__list">
        <li class="contact__item">
          <svg class="contact__icon" viewBox="0 0 24 24" aria-hidden="true"><path d="M6.6 2.5l3 3.2-1.8 2.6c1.3 3 3.4 5.2 6.4 6.6l2.5-1.9 3.3 3-1.6 3.5C11.2 19.8 4.4 13 3.1 4.2z"/></svg>
          <span>07912358046</span>
        </li>
        <li class="contact__item">
          <svg class="contact__icon" viewBox="0 0 24 24" aria-hidden="true"><path d="M2 5h20v2l-10 6L2 7z M2 9.3l10 6 10-6V19H2z"/></svg>
          <span>owen@brindleoffers.co.uk</span>
        </li>
      </ul>
    </div>
    <ul class="socials">
      <li class="socials__item"><span class="socials__dot socials__dot--chatter"></span>Chatterbook</li>
      <li class="socials__item"><span class="socials__dot socials__dot--pipline"></span>Pipline</li>
      <li class="socials__item"><span class="socials__dot socials__dot--snapa"></span>Snapa</li>
    </ul>
  </section>

  <section class="card card--back" aria-label="Business card back">
    <svg class="back-art" viewBox="0 0 700 400" width="700" height="400">
      <defs>
        <path id="url-arc" d="M250 190 A100 100 0 0 1 450 190"/>
      </defs>
      <text class="back-url">
        <textPath href="#url-arc" startOffset="50%" text-anchor="middle">www.brindleoffers.co.uk</textPath>
      </text>
      <circle cx="350" cy="200" r="78" fill="none" stroke="var(--ring-grey)" stroke-width="6"/>
      <text class="back-name" x="350" y="330" text-anchor="middle">Brindle Offers</text>
    </svg>
  </section>
</main>
</body>
</html>
```